BRIGHTWELL PARTNERS POWERPOINT PRESENTATION TEMPLATE 1

We need the ultimate quality Powerpoint presentation design.
We are the advisory firm working with modern world class tech companies throughout Europe, their founders, shareholders, and potential investors.
The new template must contain elements such as our logo, appropriate backgrounds, be at the same time very attractive visually and easy to rear. Also there must be some place where logo of our clients should be placed.

We like:
- icons and
- infographics,
so attractive design in this area will be greatly appreciated.

Please avoid serif fonts and excessive decorations such as "waves" or other similar decor.

We are also in contact with serious investors - wealthy individuals, reputable financial institutions, and their advisers; banks, private equity investors, global technology companies.

The Powerpoint template design must send a message that:
- we are a high technology oriented team of professionals,
- we provide modern financial advisory services
- but at the same time we are open minded, creative, yet very competent in the area of corporate finance.

The Powerpoint template must complement our business card design, first impression of a team of top notch professionals who advise top notch tech companies on their top notch corporate finance and M&A projects.

Enclosed are sets of our logo, current template, business card project which won previous competition.

It is perhaps a good basis to start with and get us to the template of our dreams.

While working on this project please think about the following firms which at some point may be looking at your design:
- Quorra
- Veltrix
- Pondero
- Zentaro (Brixel)
- Moodlane
- Kurotan
- Wavoro
- Dalvion
- Strelo

The quality of the design, its style, aesthetics must meet the top criteria in contemporary design trends.

Target Market(s)

Banks, financial investors, strategic investors

Industry/Entity Type

Finance

Font styles to use
Sans Serif

Requirements
Must have
• Icons
Infographics
Attractive backgrounds
Clean design
Harmonize with logo and emblem colors.
Should not have
• Excessive tacky decor (waves, etc)
Serif fonts
Excessive colors

```html
<!DOCTYPE html>
<html lang="en">
<head>
<meta charset="utf-8">
<title>Brightwell Partners – Presentation Template</title>
<link href="https://fonts.googleapis.com/css2?family=Montserrat:wght@300;400;600;700;800&family=Open+Sans:wght@400;600;700&display=swap" rel="stylesheet">
<style>
:root{
  --navy:#0f2d5e;
  --deep:#0b2350;
  --blue:#1f5fb5;
  --bright:#2b78d2;
  --sky:#4a8fe0;
  --grey:#e8eaee;
  --mid:#b9bfc8;
  --text:#5b6370;
  --white:#fff;
  --stage:#e6e7ea;
  --mapfill:#dbe3ef;
}
*{box-sizing:border-box;margin:0;padding:0}
html,body{width:1200px;height:2337px;overflow:hidden;background:#fff}
body{position:relative;font-family:"Open Sans",sans-serif;color:var(--text)}
.icon-set{position:absolute;width:0;height:0;overflow:hidden}
.stage{position:absolute;left:0;top:0;width:1200px;height:508px;background:var(--stage)}
.cover{position:absolute;left:363px;top:68px;width:471px;height:266px;background:linear-gradient(135deg,#2672cb,#1a4fa0);color:#fff;font-family:"Montserrat",sans-serif;overflow:hidden}
.cover .name{position:absolute;left:45px;top:86px;font-size:17px;font-weight:300;letter-spacing:.5px}
.cover .desc{position:absolute;left:45px;top:126px;font-size:14.5px;font-weight:300;line-height:18px}
.cover .desc b{font-weight:800}
.cover .date{position:absolute;left:49px;top:215px;font-size:7.5px}

.slide{position:absolute;width:385px;height:216px;background:#fff;overflow:hidden;box-shadow:0 0 0 .5px #dfe2e7}
.c1{left:14.5px}.c2{left:407px}.c3{left:801px}
.r1{top:508px}.r2{top:736.5px}.r3{top:965px}.r4{top:1193.5px}.r5{top:1422px}.r6{top:1650.5px}.r7{top:1879px}.r8{top:2108px}
.s-title{position:absolute;left:15px;top:8px;font-family:"Montserrat",sans-serif;font-weight:800;font-size:8.2px;color:var(--navy)}
.s-sub{position:absolute;left:15px;top:17px;font-family:"Montserrat",sans-serif;font-size:3.6px;letter-spacing:2px;color:#9aa2ae}
.s-rule{position:absolute;left:15px;top:25px;width:20px;height:1.5px;background:var(--blue)}
.brand{position:absolute;right:10px;top:10px;display:flex;align-items:center;gap:2px;font-family:"Montserrat",sans-serif;font-size:5.6px;font-weight:400;color:var(--navy)}
.brand i{width:6px;height:6px;border-radius:50%;border:1.4px solid var(--blue);display:block}
.footer{position:absolute;left:0;bottom:0;width:100%;height:7px;background:linear-gradient(90deg,var(--deep),var(--blue));display:flex;align-items:center;justify-content:space-between;font-size:3.2px;color:#fff;letter-spacing:1.6px;font-family:"Montserrat",sans-serif}
.footer span:first-child{padding-left:8px}
.footer span:last-child{background:#3f71b8;height:100%;width:58px;display:flex;align-items:center;justify-content:center;letter-spacing:0}
.tiny{font-size:3.6px;line-height:4.6px;color:#7d8591}
.lbl{font-family:"Montserrat",sans-serif;font-weight:700;font-size:5px;color:var(--navy)}
.photo{position:absolute}
.ico{position:absolute;width:16px;height:16px;border-radius:50%;background:var(--navy);box-shadow:0 0 0 2px #dfe6f1;color:#fff}
.ico svg,.tile svg{position:absolute;left:22%;top:22%;width:56%;height:56%}
.ico.outline{background:transparent;box-shadow:none;border:1px solid #fff}
.tile{position:absolute;width:56px;height:56px;background:#fff;box-shadow:0 1px 5px rgba(0,0,0,.15);text-align:center;padding-top:34px;color:var(--navy)}
.tile svg{left:18px;top:10px;width:20px;height:20px;color:#8d96a3}
.tile.on{background:linear-gradient(160deg,var(--bright),var(--navy));color:#fff;box-shadow:0 1px 5px rgba(0,0,0,.25)}
.tile.on svg{color:#fff}
.tile.on .tiny{color:#fff}
.bcard{position:absolute;background:linear-gradient(160deg,var(--bright),var(--navy));color:#fff}
.bcard .lbl{color:#fff}
.bcard .tiny{color:#dbe6f6}
.num{position:absolute;width:11px;height:11px;border-radius:50%;background:var(--navy);color:#fff;font-size:4px;font-weight:700;display:flex;align-items:center;justify-content:center}
.big-title{font-family:"Montserrat",sans-serif;font-weight:800;color:var(--navy)}
.year{position:absolute;width:60px;height:6px;border-radius:3px;color:#fff;font-size:4px;font-weight:700;padding-left:3px;line-height:6px}
</style>
</head>
<body>

<svg class="icon-set" aria-hidden="true">
  <symbol id="i-chart" viewBox="0 0 24 24" fill="none" stroke="currentColor" stroke-width="2"><path d="M3 21h18M6 17v-5M11 17V8M16 17v-7M20 17V5"/></symbol>
  <symbol id="i-bulb" viewBox="0 0 24 24" fill="none" stroke="currentColor" stroke-width="2"><path d="M9 18h6M10 21h4M12 3a6 6 0 0 0-3.5 10.9V16h7v-2.1A6 6 0 0 0 12 3z"/></symbol>
  <symbol id="i-gear" viewBox="0 0 24 24" fill="none" stroke="currentColor" stroke-width="2"><circle cx="12" cy="12" r="3.5"/><path d="M12 2v3M12 19v3M2 12h3M19 12h3M4.9 4.9l2.1 2.1M17 17l2.1 2.1M4.9 19.1L7 17M17 7l2.1-2.1"/></symbol>
  <symbol id="i-user" viewBox="0 0 24 24" fill="none" stroke="currentColor" stroke-width="2"><circle cx="12" cy="8" r="4"/><path d="M4 21c0-4.4 3.6-7 8-7s8 2.6 8 7"/></symbol>
  <symbol id="i-doc" viewBox="0 0 24 24" fill="none" stroke="currentColor" stroke-width="2"><path d="M6 2h9l4 4v16H6z"/><path d="M9 11h7M9 15h7M9 19h5"/></symbol>
  <symbol id="i-flag" viewBox="0 0 24 24" fill="none" stroke="currentColor" stroke-width="2"><path d="M5 22V3M5 4h13l-3 4 3 4H5"/></symbol>
  <symbol id="i-brief" viewBox="0 0 24 24" fill="none" stroke="currentColor" stroke-width="2"><rect x="3" y="7" width="18" height="13" rx="1"/><path d="M9 7V4h6v3M3 13h18"/></symbol>
  <symbol id="i-check" viewBox="0 0 24 24" fill="none" stroke="currentColor" stroke-width="2"><circle cx="12" cy="12" r="9"/><path d="M8 12l3 3 5-6"/></symbol>
  <symbol id="i-eye" viewBox="0 0 24 24" fill="none" stroke="currentColor" stroke-width="2"><path d="M2 12s4-7 10-7 10 7 10 7-4 7-10 7S2 12 2 12z"/><circle cx="12" cy="12" r="3"/></symbol>
  <symbol id="i-trend" viewBox="0 0 24 24" fill="none" stroke="currentColor" stroke-width="2"><path d="M3 18l6-6 4 4 8-9M15 7h6v6"/></symbol>
  <symbol id="i-coin" viewBox="0 0 24 24" fill="none" stroke="currentColor" stroke-width="2"><circle cx="12" cy="12" r="9"/><path d="M15 9h-4a2 2 0 0 0 0 4h2a2 2 0 0 1 0 4H9M12 6v2M12 17v2"/></symbol>
  <symbol id="i-steps" viewBox="0 0 24 24" fill="none" stroke="currentColor" stroke-width="2"><path d="M3 21h5v-5h5v-5h5V6h3M3 21v-3"/></symbol>
</svg>

<section class="stage">
  <div class="cover">
    <div class="name">BRIGHTWELL PARTNERS</div>
    <div class="desc">[BRIEF DESCRIPTION OF<br>THE COMPANY.<br><b>ONE-TWO SENTENCES</b>]</div>
    <div class="date">[MONTH,YEAR]</div>
  </div>
</section>

<!-- Row 1 -->
<section class="slide c1 r1">
  <div class="photo" role="img" aria-label="Faded office interior photograph" style="left:0;top:0;width:385px;height:216px;background:linear-gradient(90deg,#dfe3e9,#f7f8fa 60%,#fff)"></div>
  <div style="position:absolute;left:0;width:385px;top:44px;text-align:center">
    <div class="brand" style="position:static;justify-content:center;font-size:9px"><i style="width:9px;height:9px"></i>BRIGHTWELL PARTNERS</div>
    <div class="big-title" style="font-size:17px;margin-top:30px">PRESENTATION TITLE</div>
    <div style="font-family:Montserrat,sans-serif;font-size:8px;color:var(--navy)">SUBTITLE GOES HERE</div>
    <div style="margin:36px auto 0;width:94px;height:15px;border-radius:8px;background:#c4c9d1;color:#fff;font-size:5px;line-height:15px">PRESENTER NAME</div>
  </div>
</section>

<section class="slide c2 r1">
  <div class="brand"><i></i>BRIGHTWELL PARTNERS</div>
  <div class="brand" style="left:25px;right:auto;top:52px;font-size:8px"><i style="width:8px;height:8px"></i>BRIGHTWELL PARTNERS</div>
  <div class="big-title" style="position:absolute;left:25px;top:80px;font-size:12px">YOUR TEXT HERE</div>
  <p class="tiny" style="position:absolute;left:25px;top:100px;width:130px;color:#333"><b>Lorem ipsum dolor sit amet</b>, consectetur adipiscing elit. Fusce sit amet neque sodales, faucibus ex eu, efficitur lacus. Cras imperdiet, nulla nec sagittis pulvinar, neque augue iaculis risus, ac fringilla felis urna fermentum mi. Ut vehicula vel enim sit amet vulputate aenean malesuada.</p>
  <p class="tiny" style="position:absolute;left:175px;top:50px;width:190px;color:#333"><b>Lorem ipsum dolor sit amet</b>, consectetur adipiscing elit. Fusce sit amet neque sodales, faucibus ex eu, efficitur lacus. Cras imperdiet, nulla nec sagittis pulvinar, neque augue iaculis risus, ac fringilla felis urna fermentum mi. Ut vehicula vel enim sit amet vulputate. Aenean malesuada consectetur diam, ac convallis quam tincidunt eget. Nam vitae elementum ipsum.<br><br><b>Maecenas in purus at tellus tincidunt sodales eu sed nibh.</b> Aenean justo elit, commodo vel felis ac, malesuada sodales purus. Nunc sollicitudin sed justo in eleifend. Fusce dictum ornare ligula, eu porttitor elit ullamcorper non. Aliquam erat volutpat. Mauris malesuada turpis non tellus scelerisque tempus.</p>
  <div class="footer"><span>STRICTLY CONFIDENTIAL</span><span>[Company logo]</span></div>
</section>

<section class="slide c3 r1">
  <div class="brand"><i></i>BRIGHTWELL PARTNERS</div>
  <div class="ico" style="left:18px;top:20px"><svg><use href="#i-flag"/></svg></div>
  <div class="lbl" style="position:absolute;left:50px;top:11px">MISSION</div>
  <p class="tiny" style="position:absolute;left:50px;top:19px;width:135px">Lorem ipsum dolor sit amet, consectetur adipiscing elit, sed do eiusmod tempor incididunt ut labore et dolore magna aliqua.</p>
  <div class="bcard" style="left:0;top:62px;width:214px;height:48px;border-radius:0 8px 8px 0;background:linear-gradient(90deg,var(--bright),var(--navy))">
    <div class="ico outline" style="left:16px;top:16px"><svg><use href="#i-eye"/></svg></div>
    <div class="lbl" style="position:absolute;left:50px;top:8px">VISION</div>
    <p class="tiny" style="position:absolute;left:50px;top:16px;width:145px;color:#dbe6f6">Lorem ipsum dolor sit amet, consectetur adipiscing elit, sed do eiusmod tempor incididunt ut labore et dolore magna aliqua.</p>
  </div>
  <div class="ico" style="left:18px;top:158px"><svg><use href="#i-steps"/></svg></div>
  <div class="lbl" style="position:absolute;left:50px;top:154px">GOAL</div>
  <p class="tiny" style="position:absolute;left:50px;top:162px;width:135px">Lorem ipsum dolor sit amet, consectetur adipiscing elit, sed do eiusmod tempor incididunt ut labore et dolore magna aliqua.</p>
  <div style="position:absolute;left:232px;top:86px;width:2px;height:30px;background:var(--blue)"></div>
  <div class="big-title" style="position:absolute;left:240px;top:86px;font-size:12px;line-height:14px">MISSION, VISION<br>&amp; GOAL</div>
  <div class="footer"><span>STRICTLY CONFIDENTIAL</span><span>[Company logo]</span></div>
</section>

<!-- Row 2 -->
<section class="slide c1 r2">
  <div class="s-title">YOUR AWESOME TEXT GOES HERE</div><div class="s-sub">SUB TITLE GOES HERE</div><div class="s-rule"></div>
  <div class="brand"><i></i>BRIGHTWELL PARTNERS</div>
  <p class="tiny" style="position:absolute;left:20px;top:50px;width:145px;color:var(--blue);font-weight:600;font-size:4.6px;line-height:5.6px">Lorem ipsum dolor sit amet, consectetur adipiscing elit, sed do eiusmod tempor incididunt ut labore et dolore magna aliqua. Lorem ipsum dolor sit amet, consectetur adipiscing elit, sed do eiusmod tempor incididunt ut labore et dolore magna aliqua.</p>
  <div style="position:absolute;left:20px;top:100px;width:145px">
    <p class="tiny" style="margin-bottom:9px">● Lorem ipsum dolor sit amet, consectetur adipiscing elit, sed do eiusmod tempor incididunt ut labore.</p>
    <p class="tiny" style="margin-bottom:9px">● Lorem ipsum dolor sit amet, consectetur adipiscing elit, sed do eiusmod tempor incididunt ut labore.</p>
    <p class="tiny" style="margin-bottom:9px">● Lorem ipsum dolor sit amet, consectetur adipiscing elit, sed do eiusmod tempor incididunt ut labore.</p>
    <p class="tiny">● Lorem ipsum dolor sit amet, consectetur adipiscing elit, sed do eiusmod tempor incididunt ut labore.</p>
  </div>
  <div class="photo" role="img" aria-label="Glass office towers seen from below" style="left:192px;top:48px;width:193px;height:128px;background:linear-gradient(160deg,#c9d7e8,#4b6d96 55%,#1e3452)"></div>
  <div class="footer"><span>STRICTLY CONFIDENTIAL</span><span>[Company logo]</span></div>
</section>

<section class="slide c2 r2">
  <div class="s-title">YOUR AWESOME TEXT GOES HERE</div><div class="s-sub">SUB TITLE GOES HERE</div><div class="s-rule"></div>
  <div class="brand"><i></i>BRIGHTWELL PARTNERS</div>
  <div class="ico" style="left:42px;top:57px"><svg><use href="#i-trend"/></svg></div><div class="lbl" style="position:absolute;left:68px;top:52px">Project name</div><p class="tiny" style="position:absolute;left:68px;top:59px;width:100px">Lorem ipsum dolor sit amet, nec an dictas equidem appellantur, ut has commune accommodare.</p>
  <div class="ico" style="left:42px;top:98px"><svg><use href="#i-brief"/></svg></div><div class="lbl" style="position:absolute;left:68px;top:93px">Project name</div><p class="tiny" style="position:absolute;left:68px;top:100px;width:100px">Lorem ipsum dolor sit amet, nec an dictas equidem appellantur, ut has commune accommodare.</p>
  <div class="ico" style="left:208px;top:57px"><svg><use href="#i-chart"/></svg></div><div class="lbl" style="position:absolute;left:234px;top:52px">Project name</div><p class="tiny" style="position:absolute;left:234px;top:59px;width:100px">Lorem ipsum dolor sit amet, nec an dictas equidem appellantur, ut has commune accommodare.</p>
  <div class="ico" style="left:208px;top:98px"><svg><use href="#i-bulb"/></svg></div><div class="lbl" style="position:absolute;left:234px;top:93px">Project name</div><p class="tiny" style="position:absolute;left:234px;top:100px;width:100px">Lorem ipsum dolor sit amet, nec an dictas equidem appellantur, ut has commune accommodare.</p>
  <div style="position:absolute;left:0;top:140px;width:385px;height:69px;background:linear-gradient(90deg,var(--blue),var(--navy))">
    <p class="tiny" style="position:absolute;left:42px;top:14px;width:140px;color:#dbe6f6">Lorem Ipsum the printing and typesetting industry. Lorem Ipsum has been the industry's standard dummy text ever since the 1500s, when an unknown printer took a galley of type and scrambled it.</p>
    <p class="tiny" style="position:absolute;left:204px;top:14px;width:145px;color:#dbe6f6">Lorem Ipsum the printing and typesetting industry. Lorem Ipsum has been the industry's standard dummy text ever since the 1500s, when an unknown printer took a galley of type.</p>
  </div>
  <div class="footer"><span>STRICTLY CONFIDENTIAL</span><span>[Company logo]</span></div>
</section>

<section class="slide c3 r2">
  <div class="s-title">YOUR AWESOME TEXT GOES HERE</div><div class="s-sub">SUB TITLE GOES HERE</div><div class="s-rule"></div>
  <div class="brand"><i></i>BRIGHTWELL PARTNERS</div>
  <div class="ico" style="left:38px;top:68px"><svg><use href="#i-trend"/></svg></div><div class="lbl" style="position:absolute;left:64px;top:62px">Project name</div><p class="tiny" style="position:absolute;left:64px;top:69px;width:100px">Lorem ipsum dolor sit amet, nec an dictas equidem appellantur, ut has commune.</p>
  <div class="ico" style="left:38px;top:108px"><svg><use href="#i-brief"/></svg></div><div class="lbl" style="position:absolute;left:64px;top:102px">Project name</div><p class="tiny" style="position:absolute;left:64px;top:109px;width:100px">Lorem ipsum dolor sit amet, nec an dictas equidem appellantur, ut has commune.</p>
  <div class="ico" style="left:38px;top:148px"><svg><use href="#i-coin"/></svg></div><div class="lbl" style="position:absolute;left:64px;top:142px">Project name</div><p class="tiny" style="position:absolute;left:64px;top:149px;width:100px">Lorem ipsum dolor sit amet, nec an dictas equidem appellantur, ut has commune.</p>
  <div class="ico" style="left:204px;top:68px"><svg><use href="#i-chart"/></svg></div><div class="lbl" style="position:absolute;left:230px;top:62px">Project name</div><p class="tiny" style="position:absolute;left:230px;top:69px;width:100px">Lorem ipsum dolor sit amet, nec an dictas equidem appellantur, ut has commune.</p>
  <div class="ico" style="left:204px;top:108px"><svg><use href="#i-user"/></svg></div><div class="lbl" style="position:absolute;left:230px;top:102px">Project name</div><p class="tiny" style="position:absolute;left:230px;top:109px;width:100px">Lorem ipsum dolor sit amet, nec an dictas equidem appellantur, ut has commune.</p>
  <div class="ico" style="left:204px;top:148px"><svg><use href="#i-doc"/></svg></div><div class="lbl" style="position:absolute;left:230px;top:142px">Project name</div><p class="tiny" style="position:absolute;left:230px;top:149px;width:100px">Lorem ipsum dolor sit amet, nec an dictas equidem appellantur, ut has commune.</p>
  <div class="footer"><span>STRICTLY CONFIDENTIAL</span><span>[Company logo]</span></div>
</section>

<!-- Row 3 -->
<section class="slide c1 r3">
  <div class="s-title">YOUR AWESOME TEXT GOES HERE</div><div class="s-sub">SUB TITLE GOES HERE</div><div class="s-rule"></div>
  <div class="brand"><i></i>BRIGHTWELL PARTNERS</div>
  <div class="num" style="left:25px;top:68px">01</div><div class="lbl" style="position:absolute;left:45px;top:67px;font-weight:600">Your Text Here</div><p class="tiny" style="position:absolute;left:45px;top:75px">Lorem ipsum dolor sit amet.</p>
  <div class="num" style="left:25px;top:96px">04</div><div class="lbl" style="position:absolute;left:45px;top:95px;font-weight:600">Your Text Here</div><p class="tiny" style="position:absolute;left:45px;top:103px">Lorem ipsum dolor sit amet.</p>
  <div class="num" style="left:25px;top:125px">07</div><div class="lbl" style="position:absolute;left:45px;top:124px;font-weight:600">Your Text Here</div><p class="tiny" style="position:absolute;left:45px;top:132px">Lorem ipsum dolor sit amet.</p>
  <div class="num" style="left:25px;top:153px">10</div><div class="lbl" style="position:absolute;left:45px;top:152px;font-weight:600">Your Text Here</div><p class="tiny" style="position:absolute;left:45px;top:160px">Lorem ipsum dolor sit amet.</p>
  <div class="num" style="left:136px;top:68px">02</div><div class="lbl" style="position:absolute;left:156px;top:67px;font-weight:600">Your Text Here</div><p class="tiny" style="position:absolute;left:156px;top:75px">Lorem ipsum dolor sit amet.</p>
  <div class="num" style="left:136px;top:96px">05</div><div class="lbl" style="position:absolute;left:156px;top:95px;font-weight:600">Your Text Here</div><p class="tiny" style="position:absolute;left:156px;top:103px">Lorem ipsum dolor sit amet.</p>
  <div class="num" style="left:136px;top:125px">08</div><div class="lbl" style="position:absolute;left:156px;top:124px;font-weight:600">Your Text Here</div><p class="tiny" style="position:absolute;left:156px;top:132px">Lorem ipsum dolor sit amet.</p>
  <div class="num" style="left:136px;top:153px">11</div><div class="lbl" style="position:absolute;left:156px;top:152px;font-weight:600">Your Text Here</div><p class="tiny" style="position:absolute;left:156px;top:160px">Lorem ipsum dolor sit amet.</p>
  <div class="num" style="left:250px;top:68px">03</div><div class="lbl" style="position:absolute;left:270px;top:67px;font-weight:600">Your Text Here</div><p class="tiny" style="position:absolute;left:270px;top:75px">Lorem ipsum dolor sit amet.</p>
  <div class="num" style="left:250px;top:96px">06</div><div class="lbl" style="position:absolute;left:270px;top:95px;font-weight:600">Your Text Here</div><p class="tiny" style="position:absolute;left:270px;top:103px">Lorem ipsum dolor sit amet.</p>
  <div class="num" style="left:250px;top:125px">09</div><div class="lbl" style="position:absolute;left:270px;top:124px;font-weight:600">Your Text Here</div><p class="tiny" style="position:absolute;left:270px;top:132px">Lorem ipsum dolor sit amet.</p>
  <div class="num" style="left:250px;top:153px">12</div><div class="lbl" style="position:absolute;left:270px;top:152px;font-weight:600">Your Text Here</div><p class="tiny" style="position:absolute;left:270px;top:160px">Lorem ipsum dolor sit amet.</p>
  <div class="footer"><span>STRICTLY CONFIDENTIAL</span><span>[Company logo]</span></div>
</section>

<section class="slide c2 r3">
  <div class="s-title">YOUR AWESOME TEXT GOES HERE</div><div class="s-sub">SUB TITLE GOES HERE</div><div class="s-rule"></div>
  <div class="brand"><i></i>BRIGHTWELL PARTNERS</div>
  <div style="position:absolute;left:50px;top:113px;width:290px;height:1px;background:#9aa7b8"></div>
  <svg style="position:absolute;left:0;top:0" width="385" height="216" fill="var(--navy)"><path d="M46 100h6l-3-5zM183 100h6l-3-5zM320 100h6l-3-5zM114 128h6l-3 5zM251 128h6l-3 5z"/></svg>
  <div class="ico" style="left:41px;top:105px;background:var(--deep)"><svg><use href="#i-flag"/></svg></div>
  <div class="ico" style="left:109px;top:105px;background:var(--navy)"><svg><use href="#i-chart"/></svg></div>
  <div class="ico" style="left:178px;top:105px;background:var(--bright)"><svg><use href="#i-doc"/></svg></div>
  <div class="ico" style="left:246px;top:105px;background:var(--mid)"><svg><use href="#i-user"/></svg></div>
  <div class="ico" style="left:315px;top:105px;background:var(--deep)"><svg><use href="#i-bulb"/></svg></div>
  <div class="lbl" style="position:absolute;left:24px;width:70px;text-align:center;top:56px">Content Title here</div><p class="tiny" style="position:absolute;left:24px;top:64px;width:70px;text-align:center">Lorem ipsum dolor sit amet, nec an dictas equidem.</p>
  <div class="lbl" style="position:absolute;left:151px;width:70px;text-align:center;top:56px">Content Title here</div><p class="tiny" style="position:absolute;left:151px;top:64px;width:70px;text-align:center">Lorem ipsum dolor sit amet, nec an dictas equidem.</p>
  <div class="lbl" style="position:absolute;left:288px;width:70px;text-align:center;top:56px">Content Title here</div><p class="tiny" style="position:absolute;left:288px;top:64px;width:70px;text-align:center">Lorem ipsum dolor sit amet, nec an dictas equidem.</p>
  <div class="lbl" style="position:absolute;left:82px;width:70px;text-align:center;top:145px">Content Title here</div><p class="tiny" style="position:absolute;left:82px;top:153px;width:70px;text-align:center">Promotion an purseves usthervise my high what.</p>
  <div class="lbl" style="position:absolute;left:219px;width:70px;text-align:center;top:145px">Content Title here</div><p class="tiny" style="position:absolute;left:219px;top:153px;width:70px;text-align:center">Promotion an purseves usthervise my high what.</p>
  <div class="footer"><span>STRICTLY CONFIDENTIAL</span><span>[Company logo]</span></div>
</section>

<section class="slide c3 r3">
  <div class="s-title">YOUR AWESOME TEXT GOES HERE</div><div class="s-sub">SUB TITLE GOES HERE</div><div class="s-rule"></div>
  <div class="brand"><i></i>BRIGHTWELL PARTNERS</div>
  <svg style="position:absolute;left:0;top:0" width="385" height="216"><path d="M60 100 L78 63 M65 122 L109 93 M65 128 L107 135 M58 136 L78 165" stroke="#9aa7b8" stroke-width=".8"/></svg>
  <div style="position:absolute;left:19px;top:92px;width:50px;height:50px;border-radius:50%;background:var(--deep);color:#fff;font-family:Montserrat,sans-serif;font-weight:800;font-size:4.2px;text-align:center;line-height:5px;padding-top:15px">YOUR<br>AWESOME<br>TEXT GOES<br>HERE</div>
  <div class="num" style="left:69px;top:52px;width:22px;height:22px;background:var(--bright);font-size:6px">01</div>
  <div class="num" style="left:100px;top:82px;width:22px;height:22px;background:var(--bright);font-size:6px">02</div>
  <div class="num" style="left:99px;top:124px;width:22px;height:22px;background:var(--bright);font-size:6px">03</div>
  <div class="num" style="left:69px;top:155px;width:22px;height:22px;background:var(--navy);font-size:6px">04</div>
  <div style="position:absolute;left:177px;top:56px;width:175px">
    <div style="position:relative;height:22px;margin-bottom:7px;box-shadow:0 1px 3px rgba(0,0,0,.15)"><div class="num" style="left:-5px;top:5px">01</div><p class="tiny" style="padding:3px 4px 0 12px">Lorem ipsum dolor sit amet, consectetur adipiscing elit, sed do eiusmod tempor incididunt ut labore et dolore magna aliqua.</p></div>
    <div style="position:relative;height:22px;margin-bottom:7px;box-shadow:0 1px 3px rgba(0,0,0,.15)"><div class="num" style="left:-5px;top:5px">02</div><p class="tiny" style="padding:3px 4px 0 12px">Lorem ipsum dolor sit amet, consectetur adipiscing elit, sed do eiusmod tempor incididunt ut labore et dolore magna aliqua.</p></div>
    <div style="position:relative;height:22px;margin-bottom:7px;box-shadow:0 1px 3px rgba(0,0,0,.15)"><div class="num" style="left:-5px;top:5px">03</div><p class="tiny" style="padding:3px 4px 0 12px">Lorem ipsum dolor sit amet, consectetur adipiscing elit, sed do eiusmod tempor incididunt ut labore et dolore magna aliqua.</p></div>
    <div style="position:relative;height:22px;box-shadow:0 1px 3px rgba(0,0,0,.15)"><div class="num" style="left:-5px;top:5px">04</div><p class="tiny" style="padding:3px 4px 0 12px">Lorem ipsum dolor sit amet, consectetur adipiscing elit, sed do eiusmod tempor incididunt ut labore et dolore magna aliqua.</p></div>
  </div>
  <div class="footer"><span>STRICTLY CONFIDENTIAL</span><span>[Company logo]</span></div>
</section>

<!-- Row 4 -->
<section class="slide c1 r4">
  <div class="brand"><i></i>BRIGHTWELL PARTNERS</div>
  <div class="s-rule" style="left:15px;top:18px"></div>
  <div class="big-title" style="position:absolute;left:20px;top:32px;font-size:9.5px;line-height:12px">LOREM IPSUM DOLOR SIT<br>AMET ELIT ET DOLOR</div>
  <p class="tiny" style="position:absolute;left:20px;top:63px;width:140px">Lorem ipsum dolor sit amet, consectetur adipiscing elit, sed do eiusmod tempor incididunt ut labore et dolore magna aliqua. Lorem ipsum dolor sit amet, consectetur adipiscing elit, sed do eiusmod.</p>
  <div class="photo" role="img" aria-label="Business meeting in a bright office" style="left:171px;top:32px;width:204px;height:110px;background:linear-gradient(135deg,#d6d8dc,#7f858e 60%,#3d434b)"></div>
  <div class="bcard" style="left:0;top:142px;width:128px;height:74px;background:var(--blue)"><div class="lbl" style="position:absolute;left:15px;top:26px">Lorem ipsum dolor</div><p class="tiny" style="position:absolute;left:15px;top:36px;width:100px">Lorem ipsum dolor sit amet, consectetur adipiscing elit, sed do eiusmod tempor incididunt ut labore.</p></div>
  <div class="bcard" style="left:128px;top:142px;width:129px;height:74px;background:var(--bright)"><div class="lbl" style="position:absolute;left:14px;top:26px">Lorem ipsum dolor</div><p class="tiny" style="position:absolute;left:14px;top:36px;width:100px">Lorem ipsum dolor sit amet, consectetur adipiscing elit, sed do eiusmod tempor incididunt ut labore.</p></div>
  <div class="bcard" style="left:257px;top:142px;width:128px;height:74px;background:var(--deep)"><div class="lbl" style="position:absolute;left:14px;top:26px">Lorem ipsum dolor</div><p class="tiny" style="position:absolute;left:14px;top:36px;width:100px">Lorem ipsum dolor sit amet, consectetur adipiscing elit, sed do eiusmod tempor incididunt ut labore.</p></div>
  <div class="ico" style="left:30px;top:128px;width:24px;height:24px;background:var(--blue);box-shadow:none"><svg><use href="#i-coin"/></svg></div>
  <div class="ico" style="left:158px;top:126px;width:24px;height:24px;background:var(--bright);box-shadow:none"><svg><use href="#i-chart"/></svg></div>
  <div class="ico" style="left:285px;top:128px;width:24px;height:24px;background:var(--deep);box-shadow:none"><svg><use href="#i-brief"/></svg></div>
</section>

<section class="slide c2 r4" style="background:linear-gradient(180deg,var(--blue) 0,var(--navy) 50%,#fff 50%)">
  <div class="big-title" style="position:absolute;left:0;width:385px;top:38px;text-align:center;color:#fff;font-size:15px">YOUR AWESOME TEXT HERE</div>
  <div style="position:absolute;left:0;width:385px;top:55px;text-align:center;color:#cfe0f6;font-family:Montserrat,sans-serif;font-size:6px;letter-spacing:2px">WRITE HERE A GREAT SUBTITLE</div>
  <div style="position:absolute;left:0;top:88px;width:385px;display:flex;justify-content:space-around;padding:0 28px">
    <div style="width:68px;text-align:center"><div style="margin:0 auto;width:30px;height:30px;border-radius:50%;background:#fff;box-shadow:0 1px 4px rgba(0,0,0,.25);font-family:Montserrat,sans-serif;font-size:6.5px;line-height:30px;color:#555">Text</div><p class="tiny" style="margin-top:10px">Lorem ipsum dolor sit amet, consectetur adipiscing elit, sed do eiusmod ut labore et dolore magna aliqua.</p></div>
    <div style="width:68px;text-align:center"><div style="margin:-4px auto 0;width:38px;height:38px;border-radius:50%;background:#fff;box-shadow:0 1px 4px rgba(0,0,0,.25);font-family:Montserrat,sans-serif;font-size:8px;line-height:38px;color:#555">Text</div><p class="tiny" style="margin-top:6px">Lorem ipsum dolor sit amet, uan ar consectetur adipiscing elit, sed do eiusmod incididunt ut labore et dolore magna.</p></div>
    <div style="width:68px;text-align:center"><div style="margin:0 auto;width:30px;height:30px;border-radius:50%;background:#fff;box-shadow:0 1px 4px rgba(0,0,0,.25);font-family:Montserrat,sans-serif;font-size:6.5px;line-height:30px;color:#555">Text</div><p class="tiny" style="margin-top:10px">Lorem ipsum dolor sit amet, consectetur adipiscing elit, sed do eiusmod ut labore et dolore magna aliqua.</p></div>
    <div style="width:68px;text-align:center"><div style="margin:0 auto;width:30px;height:30px;border-radius:50%;background:#fff;box-shadow:0 1px 4px rgba(0,0,0,.25);font-family:Montserrat,sans-serif;font-size:6.5px;line-height:30px;color:#555">Text</div><p class="tiny" style="margin-top:10px">Lorem ipsum dolor sit amet, uan ar consectetur adipiscing elit, sed do eiusmod ut labore et dolore magna.</p></div>
  </div>
  <div class="footer"><span>STRICTLY CONFIDENTIAL</span><span>[Company logo]</span></div>
</section>

<section class="slide c3 r4">
  <div class="s-title">YOUR AWESOME TEXT GOES HERE</div><div class="s-sub">SUB TITLE GOES HERE</div><div class="s-rule"></div>
  <div class="brand"><i></i>BRIGHTWELL PARTNERS</div>
  <div style="position:absolute;left:34px;top:62px;width:318px;height:110px;display:flex;font-family:Montserrat,sans-serif">
    <div style="flex:1;background:#eef0f3"><div style="background:var(--navy);color:#fff;font-size:5px;font-weight:700;height:17px;line-height:17px;text-align:center">ADD YOUR TITLE</div><div style="padding:6px 8px"><div class="lbl" style="font-weight:600">Project name</div><p class="tiny">Lorem Ipsum is simply dummy unknown printer took a galley of type.</p><div class="lbl" style="font-weight:600;margin-top:8px">Project name</div><p class="tiny">Lorem Ipsum is simply dummy unknown printer took a galley of type.</p></div></div>
    <div style="flex:1;background:#e3e6ea"><div style="background:var(--navy);color:#fff;font-size:5px;font-weight:700;height:17px;line-height:17px;text-align:center">ADD YOUR TITLE</div><div style="padding:6px 8px"><div class="lbl" style="font-weight:600">Project name</div><p class="tiny">Lorem Ipsum is simply dummy unknown printer took a galley of type.</p><div class="lbl" style="font-weight:600;margin-top:8px">Project name</div><p class="tiny">Lorem Ipsum is simply dummy unknown printer took a galley of type.</p></div></div>
    <div style="flex:1;background:var(--bright);margin-top:-3px;box-shadow:0 1px 5px rgba(0,0,0,.3)"><div style="background:#fff;color:var(--navy);font-size:4.6px;height:20px;display:flex;align-items:center;justify-content:center;gap:2px"><i style="width:5px;height:5px;border-radius:50%;border:1.2px solid var(--blue);display:block"></i>BRIGHTWELL PARTNERS</div><div style="padding:6px 8px"><div class="lbl" style="font-weight:600;color:#fff">Project name</div><p class="tiny" style="color:#e0eaf8">Lorem Ipsum is simply dummy unknown printer took a galley of type.</p><div class="lbl" style="font-weight:600;margin-top:8px;color:#fff">Project name</div><p class="tiny" style="color:#e0eaf8">Lorem Ipsum is simply dummy unknown printer took a galley of type.</p></div></div>
    <div style="flex:1;background:#eef0f3"><div style="background:var(--navy);color:#fff;font-size:5px;font-weight:700;height:17px;line-height:17px;text-align:center">ADD YOUR TITLE</div><div style="padding:6px 8px"><div class="lbl" style="font-weight:600">Project name</div><p class="tiny">Lorem Ipsum is simply dummy unknown printer took a galley of type.</p><div class="lbl" style="font-weight:600;margin-top:8px">Project name</div><p class="tiny">Lorem Ipsum is simply dummy unknown printer took a galley of type.</p></div></div>
  </div>
  <div class="footer"><span>STRICTLY CONFIDENTIAL</span><span>[Company logo]</span></div>
</section>

<!-- Row 5 -->
<section class="slide c1 r5" style="background:linear-gradient(135deg,var(--bright),var(--navy))">
  <div style="position:absolute;left:14px;top:50px;font-family:Montserrat,sans-serif;font-weight:800;font-size:38px;color:rgba(255,255,255,.18)">01</div>
  <div style="position:absolute;left:33px;top:62px;font-family:Montserrat,sans-serif;font-weight:700;font-size:31px;line-height:30px;color:#fff">Slide<br>Break</div>
  <p class="tiny" style="position:absolute;left:33px;top:150px;width:190px;color:#cfe0f6">Lorem ipsum dolor sit amet, consectetur adipiscing elit, sed do eiusmod tempor incididunt ut labore et dolore magna aliqua. Ut enim ad minim veniam, quis nostrud exercitation ullamco laboris nisi ut aliquip.</p>
</section>

<section class="slide c2 r5">
  <div class="s-title">YOUR AWESOME TEXT GOES HERE</div><div class="s-sub">SUB TITLE GOES HERE</div><div class="s-rule"></div>
  <div class="brand"><i></i>BRIGHTWELL PARTNERS</div>
  <svg style="position:absolute;left:130px;top:52px" width="125" height="125" viewBox="0 0 100 100">
    <g fill="none" stroke-width="17">
      <circle cx="50" cy="50" r="33" stroke="var(--blue)" stroke-dasharray="33.5 173.8" transform="rotate(-90 50 50)"/>
      <circle cx="50" cy="50" r="33" stroke="#8a9099" stroke-dasharray="33.5 173.8" transform="rotate(-30 50 50)"/>
      <circle cx="50" cy="50" r="33" stroke="#a8aeb6" stroke-dasharray="33.5 173.8" transform="rotate(30 50 50)"/>
      <circle cx="50" cy="50" r="33" stroke="#b8bdc4" stroke-dasharray="33.5 173.8" transform="rotate(90 50 50)"/>
      <circle cx="50" cy="50" r="33" stroke="#c8ccd2" stroke-dasharray="33.5 173.8" transform="rotate(150 50 50)"/>
      <circle cx="50" cy="50" r="33" stroke="#d6d9dd" stroke-dasharray="33.5 173.8" transform="rotate(210 50 50)"/>
    </g>
    <circle cx="50" cy="50" r="19" fill="#fff"/>
    <g color="#fff">
      <use href="#i-trend" x="60" y="14" width="11" height="11"/>
      <use href="#i-user" x="76" y="44" width="11" height="11"/>
      <use href="#i-check" x="60" y="74" width="11" height="11"/>
      <use href="#i-gear" x="29" y="74" width="11" height="11"/>
      <use href="#i-doc" x="13" y="44" width="11" height="11"/>
      <use href="#i-chart" x="29" y="14" width="11" height="11"/>
    </g>
    <use href="#i-brief" x="43" y="43" width="14" height="14" color="var(--blue)"/>
  </svg>
  <div class="lbl" style="position:absolute;left:80px;top:52px;color:var(--blue)">Lorem ipsum dolor</div><p class="tiny" style="position:absolute;left:36px;top:60px;width:95px;text-align:right">Lorem ipsum dolor sit amet, consectetur adipiscing elit, sed do eiusmod tempor.</p>
  <div class="lbl" style="position:absolute;left:60px;top:105px;color:var(--blue)">Lorem ipsum dolor</div><p class="tiny" style="position:absolute;left:16px;top:113px;width:95px;text-align:right">Lorem ipsum dolor sit amet, consectetur adipiscing elit, sed do eiusmod tempor.</p>
  <div class="lbl" style="position:absolute;left:82px;top:158px;color:var(--blue)">Lorem ipsum dolor</div><p class="tiny" style="position:absolute;left:38px;top:166px;width:95px;text-align:right">Lorem ipsum dolor sit amet, consectetur adipiscing elit, sed do eiusmod tempor.</p>
  <div class="lbl" style="position:absolute;left:248px;top:50px;color:var(--blue)">Lorem ipsum dolor</div><p class="tiny" style="position:absolute;left:248px;top:58px;width:95px">Lorem ipsum dolor sit amet, consectetur adipiscing elit, sed do eiusmod tempor.</p>
  <div class="lbl" style="position:absolute;left:270px;top:104px;color:var(--blue)">Lorem ipsum dolor</div><p class="tiny" style="position:absolute;left:270px;top:112px;width:95px">Lorem ipsum dolor sit amet, consectetur adipiscing elit, sed do eiusmod tempor.</p>
  <div class="lbl" style="position:absolute;left:250px;top:156px;color:var(--blue)">Lorem ipsum dolor</div><p class="tiny" style="position:absolute;left:250px;top:164px;width:95px">Lorem ipsum dolor sit amet, consectetur adipiscing elit, sed do eiusmod tempor.</p>
  <div class="footer"><span>STRICTLY CONFIDENTIAL</span><span>[Company logo]</span></div>
</section>

<section class="slide c3 r5">
  <div class="s-title">YOUR AWESOME TEXT GOES HERE</div><div class="s-sub">SUB TITLE GOES HERE</div><div class="s-rule"></div>
  <div class="brand"><i></i>BRIGHTWELL PARTNERS</div>
  <svg style="position:absolute;left:110px;top:78px" width="165" height="70">
    <polygon points="0,35 35,5 35,18 80,18 80,52 35,52 35,65" fill="var(--bright)"/>
    <polygon points="165,35 130,5 130,18 85,18 85,52 130,52 130,65" fill="var(--deep)"/>
  </svg>
  <div style="position:absolute;left:160px;top:85px;width:62px;height:56px;border-radius:50%;background:#fff;box-shadow:0 0 6px rgba(0,0,0,.2);display:flex;align-items:center;justify-content:center;font-family:Montserrat,sans-serif;font-size:4.6px;color:var(--navy);text-align:center">BRIGHTWELL<br>PARTNERS</div>
  <div style="position:absolute;left:24px;top:75px;width:85px"><div class="lbl">Lorem ipsum dolor</div><p class="tiny">Lorem ipsum dolor sit amet, consectetur adipiscing elit, sed do eiusmod tempor.</p><p class="tiny" style="margin-top:4px">▸ Lorem ipsum dolor<br>▸ Sit amet consectetur adipiscing<br>▸ Do eiusmod tempor<br>▸ Lorem ipsum dolor</p></div>
  <div style="position:absolute;left:275px;top:75px;width:90px"><div class="lbl">Lorem ipsum dolor</div><p class="tiny">Lorem ipsum dolor sit amet, consectetur adipiscing elit, sed do eiusmod tempor.</p><p class="tiny" style="margin-top:4px">▸ Lorem ipsum dolor<br>▸ Sit amet consectetur adipiscing<br>▸ Do eiusmod tempor<br>▸ Lorem ipsum dolor</p></div>
  <div class="footer"><span>STRICTLY CONFIDENTIAL</span><span>[Company logo]</span></div>
</section>

<!-- Row 6 -->
<section class="slide c1 r6">
  <div class="brand"><i></i>BRIGHTWELL PARTNERS</div>
  <div class="s-rule" style="top:26px"></div>
  <div style="position:absolute;left:95px;top:22px;font-family:Montserrat,sans-serif;font-weight:700;font-size:15.5px;color:#111">Your Company <span style="color:var(--bright)">Timeline</span></div>
  <svg style="position:absolute;left:0;top:0" width="385" height="216"><path d="M20 34 C20 70,40 68,80 68 L360 68 C395 68,395 125,360 125 L60 125 C20 125,20 165,40 178 C60 190,300 190,350 200" fill="none" stroke="#aeb4bd" stroke-width=".8"/></svg>
  <div class="year" style="left:75px;top:68px;background:var(--blue)">2015</div>
  <div class="year" style="left:165px;top:68px;background:var(--mid)">2016</div>
  <div class="year" style="left:255px;top:68px;background:var(--blue)">2017</div>
  <div class="year" style="left:75px;top:131px;background:var(--mid)">2018</div>
  <div class="year" style="left:165px;top:131px;background:var(--blue)">2019</div>
  <div class="year" style="left:255px;top:131px;background:var(--mid)">2020</div>
  <p class="tiny" style="position:absolute;left:78px;top:78px;width:55px;color:#333">Lorem Ipsum is simply dummy unknown printer took a galley.</p>
  <p class="tiny" style="position:absolute;left:168px;top:78px;width:55px;color:#333">Lorem Ipsum is simply dummy unknown printer took a galley.</p>
  <p class="tiny" style="position:absolute;left:258px;top:78px;width:55px;color:#333">Lorem Ipsum is simply dummy unknown printer took a galley.</p>
  <p class="tiny" style="position:absolute;left:78px;top:141px;width:55px;color:#333">Lorem Ipsum is simply dummy unknown printer took a galley.</p>
  <p class="tiny" style="position:absolute;left:168px;top:141px;width:55px;color:#333">Lorem Ipsum is simply dummy unknown printer took a galley.</p>
  <p class="tiny" style="position:absolute;left:258px;top:141px;width:55px;color:#333">Lorem Ipsum is simply dummy unknown printer took a galley.</p>
  <div class="footer"><span>STRICTLY CONFIDENTIAL</span><span>[Company logo]</span></div>
</section>

<section class="slide c2 r6">
  <div class="s-title">YOUR AWESOME TEXT GOES HERE</div><div class="s-sub">SUB TITLE GOES HERE</div><div class="s-rule"></div>
  <div class="brand"><i></i>BRIGHTWELL PARTNERS</div>
  <p class="tiny" style="position:absolute;left:26px;top:46px;width:150px;color:var(--blue);font-weight:600;font-size:4.6px;line-height:5.6px">Lorem ipsum dolor sit amet, consectetur adipiscing elit, sed do eiusmod tempor incididunt ut labore et dolore magna aliqua. Lorem ipsum dolor sit amet, consectetur adipiscing elit, sed do eiusmod tempor.</p>
  <div style="position:absolute;left:26px;top:98px;width:150px">
    <p class="tiny" style="margin-bottom:9px">● Lorem ipsum dolor sit amet, consectetur adipiscing elit, sed do eiusmod tempor.</p>
    <p class="tiny" style="margin-bottom:9px">● Lorem ipsum dolor sit amet, consectetur adipiscing elit, sed do eiusmod tempor.</p>
    <p class="tiny" style="margin-bottom:9px">● Lorem ipsum dolor sit amet, consectetur adipiscing elit, sed do eiusmod tempor.</p>
    <p class="tiny">● Lorem ipsum dolor sit amet, consectetur adipiscing elit, sed do eiusmod tempor.</p>
  </div>
  <div class="tile" style="left:226px;top:50px"><svg><use href="#i-flag"/></svg><p class="tiny">Simple<br>Presentation</p></div>
  <div class="tile on" style="left:289px;top:50px"><svg><use href="#i-trend"/></svg><p class="tiny">Simple<br>Presentation</p></div>
  <div class="tile" style="left:226px;top:113px"><svg><use href="#i-bulb"/></svg><p class="tiny">Simple<br>Presentation</p></div>
  <div class="tile" style="left:289px;top:113px"><svg><use href="#i-check"/></svg><p class="tiny">Simple<br>Presentation</p></div>
  <div class="footer"><span>STRICTLY CONFIDENTIAL</span><span>[Company logo]</span></div>
</section>

<section class="slide c3 r6">
  <div class="s-title">YOUR AWESOME TEXT GOES HERE</div><div class="s-sub">SUB TITLE GOES HERE</div><div class="s-rule"></div>
  <div class="brand"><i></i>BRIGHTWELL PARTNERS</div>
  <div class="bcard" style="left:61px;top:70px;width:80px;height:107px;padding:22px 10px 0"><div style="font-family:Montserrat,sans-serif;font-weight:700;font-size:7px;line-height:8px">Add<br>Awesome<br>Title Here</div><p class="tiny" style="margin-top:5px">Lorem ipsum dolor sit amet, consectetur adipiscing elit, sed do eiusmod tempor incididunt ut labore et dolore magna aliqua.</p></div>
  <div class="bcard" style="left:152px;top:70px;width:80px;height:107px;padding:22px 10px 0"><div style="font-family:Montserrat,sans-serif;font-weight:700;font-size:7px;line-height:8px">Add<br>Awesome<br>Title Here</div><p class="tiny" style="margin-top:5px">Lorem ipsum dolor sit amet, consectetur adipiscing elit, sed do eiusmod tempor incididunt ut labore et dolore magna aliqua.</p></div>
  <div class="bcard" style="left:243px;top:70px;width:80px;height:107px;padding:22px 10px 0"><div style="font-family:Montserrat,sans-serif;font-weight:700;font-size:7px;line-height:8px">Add<br>Awesome<br>Title Here</div><p class="tiny" style="margin-top:5px">Lorem ipsum dolor sit amet, consectetur adipiscing elit, sed do eiusmod tempor incididunt ut labore et dolore magna aliqua.</p></div>
  <div class="ico" style="left:93px;top:60px;box-shadow:0 0 0 1.5px #fff"><svg><use href="#i-user"/></svg></div>
  <div class="ico" style="left:184px;top:60px;box-shadow:0 0 0 1.5px #fff"><svg><use href="#i-chart"/></svg></div>
  <div class="ico" style="left:275px;top:60px;box-shadow:0 0 0 1.5px #fff"><svg><use href="#i-gear"/></svg></div>
  <div class="footer"><span>STRICTLY CONFIDENTIAL</span><span>[Company logo]</span></div>
</section>

<!-- Row 7 -->
<section class="slide c1 r7">
  <div class="s-title">YOUR AWESOME TEXT GOES HERE</div><div class="s-sub">SUB TITLE GOES HERE</div><div class="s-rule"></div>
  <div class="brand"><i></i>BRIGHTWELL PARTNERS</div>
  <div class="photo" role="img" aria-label="Businessman presenting documents at a desk" style="left:0;top:48px;width:182px;height:136px;background:linear-gradient(135deg,#b9c6d8,#56708f 50%,#22344f)"></div>
  <div class="bcard" style="left:192px;top:48px;width:85px;height:136px;padding:60px 10px 0"><div class="ico outline" style="left:10px;top:28px"><svg><use href="#i-check"/></svg></div><div class="lbl">Project name</div><p class="tiny" style="margin-top:3px">Lorem ipsum dolor sit amet, nec an dictas equidem appellantur, ut has commune accommodare. Mea illum, ludus solet idpro.</p></div>
  <div class="bcard" style="left:286px;top:48px;width:85px;height:136px;padding:60px 10px 0"><div class="ico outline" style="left:10px;top:28px"><svg><use href="#i-trend"/></svg></div><div class="lbl">Project name</div><p class="tiny" style="margin-top:3px">Lorem ipsum dolor sit amet, nec an dictas equidem appellantur, ut has commune accommodare. Mea illum, ludus solet idpro.</p></div>
  <div class="footer"><span>STRICTLY CONFIDENTIAL</span><span>[Company logo]</span></div>
</section>

<section class="slide c2 r7">
  <div class="s-title">YOUR AWESOME TEXT GOES HERE</div><div class="s-sub">SUB TITLE GOES HERE</div><div class="s-rule"></div>
  <div class="brand"><i></i>BRIGHTWELL PARTNERS</div>
  <div class="bcard" style="left:15px;top:60px;width:174px;height:50px;background:linear-gradient(90deg,var(--blue),var(--navy))"><div class="ico outline" style="left:14px;top:12px"><svg><use href="#i-user"/></svg></div><div class="lbl" style="position:absolute;left:42px;top:9px">Project name</div><p class="tiny" style="position:absolute;left:42px;top:17px;width:122px">Lorem ipsum dolor sit amet, nec an dictas equidem appellantur, ut has commune accommodare. Mea illum, ludus solet idpro.</p></div>
  <div class="bcard" style="left:201px;top:60px;width:174px;height:50px;background:linear-gradient(90deg,var(--blue),var(--navy))"><div class="ico outline" style="left:14px;top:12px"><svg><use href="#i-trend"/></svg></div><div class="lbl" style="position:absolute;left:42px;top:9px">Project name</div><p class="tiny" style="position:absolute;left:42px;top:17px;width:122px">Lorem ipsum dolor sit amet, nec an dictas equidem appellantur, ut has commune accommodare. Mea illum, ludus solet idpro.</p></div>
  <div class="bcard" style="left:15px;top:120px;width:174px;height:50px;background:linear-gradient(90deg,var(--blue),var(--navy))"><div class="ico outline" style="left:14px;top:12px"><svg><use href="#i-chart"/></svg></div><div class="lbl" style="position:absolute;left:42px;top:9px">Project name</div><p class="tiny" style="position:absolute;left:42px;top:17px;width:122px">Lorem ipsum dolor sit amet, nec an dictas equidem appellantur, ut has commune accommodare. Mea illum, ludus solet idpro.</p></div>
  <div class="bcard" style="left:201px;top:120px;width:174px;height:50px;background:linear-gradient(90deg,var(--blue),var(--navy))"><div class="ico outline" style="left:14px;top:12px"><svg><use href="#i-gear"/></svg></div><div class="lbl" style="position:absolute;left:42px;top:9px">Project name</div><p class="tiny" style="position:absolute;left:42px;top:17px;width:122px">Lorem ipsum dolor sit amet, nec an dictas equidem appellantur, ut has commune accommodare. Mea illum, ludus solet idpro.</p></div>
  <div class="footer"><span>STRICTLY CONFIDENTIAL</span><span>[Company logo]</span></div>
</section>

<section class="slide c3 r7">
  <div class="brand"><i></i>BRIGHTWELL PARTNERS</div>
  <div style="position:absolute;left:18px;top:80px;width:2px;height:48px;background:var(--blue)"></div>
  <div class="big-title" style="position:absolute;left:27px;top:80px;font-size:12px;line-height:15.5px">YOUR<br>CUSTOMERS OR<br>COMPETITORS</div>
  <div class="s-sub" style="left:27px;top:130px">SUB TITLE GOES HERE</div>
  <svg style="position:absolute;left:160px;top:38px" width="215" height="150" viewBox="0 0 215 150" font-family="Montserrat, sans-serif" font-weight="700" font-size="6" text-anchor="middle">
    <defs><polygon id="hx" points="0,-18 15.6,-9 15.6,9 0,18 -15.6,9 -15.6,-9"/></defs>
    <g fill="#fff" stroke-width="3.5">
      <use href="#hx" x="74" y="22" stroke="#b5bcc6"/>
      <use href="#hx" x="128" y="20" stroke="var(--navy)"/>
      <use href="#hx" x="20" y="44" stroke="var(--blue)"/>
      <use href="#hx" x="56" y="50" stroke="var(--blue)"/>
      <use href="#hx" x="104" y="50" stroke="var(--navy)"/>
      <use href="#hx" x="165" y="50" stroke="var(--blue)"/>
      <use href="#hx" x="80" y="80" stroke="var(--navy)"/>
      <use href="#hx" x="130" y="80" stroke="#b5bcc6"/>
      <use href="#hx" x="40" y="110" stroke="var(--navy)"/>
      <use href="#hx" x="100" y="110" stroke="#b5bcc6"/>
      <use href="#hx" x="165" y="110" stroke="var(--blue)"/>
    </g>
    <g fill="var(--navy)">
      <text x="74" y="24">Norvik</text>
      <text x="104" y="52">Casteo</text>
      <text x="80" y="82" font-size="5.4">Banquera</text>
      <text x="128" y="22" fill="#9aa2ae" font-weight="400">Lunetta</text>
      <text x="100" y="112" fill="#9aa2ae" font-weight="400">Lunetta</text>
      <text x="165" y="112" fill="#9aa2ae" font-weight="400">Lunetta</text>
    </g>
  </svg>
  <div class="footer"><span>STRICTLY CONFIDENTIAL</span><span>[Company logo]</span></div>
</section>

<!-- Row 8 -->
<section class="slide r8" style="left:224px">
  <div class="brand"><i></i>BRIGHTWELL PARTNERS</div>
  <div class="photo" role="img" aria-label="World map with highlighted office regions" style="left:110px;top:22px;width:262px;height:178px;border-radius:4px;background:linear-gradient(135deg,var(--mapfill),#c6d3e7 60%,#a9bddc)"></div>
  <div style="position:absolute;left:18px;top:148px;width:2px;height:36px;background:var(--blue)"></div>
  <div class="big-title" style="position:absolute;left:27px;top:150px;font-size:12.5px;line-height:17px">MARK YOUR<br>LOCATIONS</div>
  <div class="footer"><span>STRICTLY CONFIDENTIAL</span><span>[Company logo]</span></div>
</section>

<section class="slide r8" style="left:620px;background:linear-gradient(135deg,var(--bright),var(--navy))">
  <div style="position:absolute;left:38px;top:48px;width:102px;font-size:4.2px;color:var(--navy)">
    <div style="height:22px;background:var(--blue);color:#fff;display:flex;align-items:center;padding-left:24px;position:relative"><svg style="position:absolute;left:8px" width="9" height="9" viewBox="0 0 10 10"><circle cx="5" cy="5" r="4" fill="none" stroke="#fff"/><path d="M1 5h8M5 1v8" stroke="#fff" stroke-width=".6"/></svg>www.brightwell.example</div>
    <div style="height:24px;margin-top:2px;background:#fff;display:flex;align-items:center;padding-left:24px;position:relative"><svg style="position:absolute;left:8px" width="9" height="10" viewBox="0 0 10 12"><path d="M5 11 C2 7 1 5.5 1 4 A4 4 0 0 1 9 4 C9 5.5 8 7 5 11Z" fill="none" stroke="var(--navy)"/><circle cx="5" cy="4" r="1.3" fill="var(--navy)"/></svg>Here to write your<br>Company adress</div>
    <div style="height:24px;margin-top:2px;background:#fff;display:flex;align-items:center;padding-left:24px;position:relative"><svg style="position:absolute;left:8px" width="9" height="9" viewBox="0 0 10 10"><path d="M2 1 L4 1 L5 3.5 L3.8 4.5 C4.5 6 5.5 7 6.5 7.6 L7.5 6.5 L9.5 7.3 L9.5 9 C5 9.5 0.8 5 1 1Z" fill="var(--navy)"/></svg>(555) 014-2277</div>
    <div style="height:24px;margin-top:2px;background:#fff;display:flex;align-items:center;padding-left:24px;position:relative"><svg style="position:absolute;left:8px" width="10" height="8" viewBox="0 0 10 8"><rect x=".5" y=".5" width="9" height="7" fill="none" stroke="var(--navy)"/><path d="M.5 .5 L5 4.5 L9.5 .5" fill="none" stroke="var(--navy)"/></svg>info@brightwell.example</div>
  </div>
  <div style="position:absolute;left:217px;top:98px;font-family:Montserrat,sans-serif;color:#fff">
    <div style="font-weight:700;font-size:20px;line-height:20px">Thank You</div>
    <div style="font-weight:400;font-size:13px;letter-spacing:1.5px">CONTACT US</div>
  </div>
</section>

</body>
</html>
```